Marlow Realty Real Estate Brokerage Recruiting Flyer

We are a real estate brokerage looking to hire more real estate agents. We need to list everything we have to offer as a company so real estate agents will join our company. this is our company website: www.Marlowrealty.example .

100% COMMISSION NO MONTHLY FEE
$450 Flat Transaction FEE

What We Offer:
24/7 Office Access
Free E & O Insurance for 1st Year
Free Online CE and PLE
Free 1,000 Business Cards
Free Professional Social Media Marketing
Free Printing, Scanning, and Copies
Free Buyer and Seller Presentation Packages
Free Filquay Cloud Based Document Management Access
Access to our Internal Brokerage Forum
Company Profit Sharing!
Private Offices Available to Rent

*Lead Generation Software with over 3,000 Leads
*10 Leads to Start
* Free Personal CRM and Website
*Restrictions and Rules apply

Company Address:
4817 Amberfield Road
Suite 512
Fairfax, VA 22194
Phone: 703-555-0147
email: info@marlowrealty.example

Target Market(s)

Real Estate Agents

Industry/Entity Type

Real Estate

Colors
0555a3
ffffff

Requirements
Must have
• 100% COMMISSION NO MONTHLY FEE
$450 Flat Transaction FEE

What We Offer:
24/7 Office Access
Free Online CE and PLE
Free 1,000 Business Cards
Company Profit Sharing!

*10 Leads to Start

Company Address:
4817 Amberfield Road
Suite 512
Fairfax, VA 22194
Phone: 703-555-0147

```html
<!DOCTYPE html>
<html lang="en">
<head>
<meta charset="utf-8">
<title>Marlow Realty – Agent Recruiting Flyer</title>
<link rel="stylesheet" href="https://fonts.googleapis.com/css2?family=Montserrat:wght@300;400;600;700;900&family=Oswald:wght@500;600&display=swap">
<style>
  :root {
    --brand-blue: #0555a3;
    --royal-blue: #1a63b8;
    --deep-navy: #0c2f6b;
    --list-blue: #2f63ad;
    --orange: #f7931e;
    --white: #ffffff;
    --footer-grey: #dcdde1;
    --stage: #ecebe8;
    --sky-top: #8fc7e6;
    --sky-mid: #cfe6f3;
  }
  * { margin: 0; padding: 0; box-sizing: border-box; }
  html, body {
    width: 1200px; height: 979px; overflow: hidden;
    background: var(--stage);
  }
  .flyer {
    position: absolute; left: 255px; top: 20px;
    width: 690px; height: 939px;
    background: var(--white);
    overflow: hidden;
    box-shadow: 0 4px 18px rgba(0,0,0,.18);
    font-family: "Montserrat", sans-serif;
  }
  .hero-photo {
    position: absolute; left: 0; top: 0; width: 690px; height: 340px;
    background:
      radial-gradient(ellipse at 62% 55%, rgba(255,235,225,.95) 0%, rgba(255,255,255,.6) 22%, rgba(255,255,255,0) 45%),
      linear-gradient(180deg, var(--sky-top) 0%, var(--sky-mid) 40%, #eaf2f6 70%, #b9d2de 100%);
  }
  .brand-name {
    position: absolute; left: 0; width: 690px; top: 62px;
    text-align: center;
    font-weight: 600; font-size: 30px; letter-spacing: 2px;
    color: var(--deep-navy);
  }
  .brand-name .mark {
    display: inline-block; width: 22px; height: 22px;
    background: var(--deep-navy); margin-right: 12px; vertical-align: -1px;
  }
  .commission-band {
    position: absolute; left: 0; top: 335px; width: 311px; height: 114px;
    background: var(--orange);
    padding: 17px 0 0 30px;
    font-family: "Oswald", sans-serif; font-weight: 600;
    font-size: 33px; line-height: 38px; color: var(--white);
  }
  .lead-panel { position: absolute; left: 0; top: 0; }
  .lead-title {
    position: absolute; top: 310px; left: 351px; width: 320px;
    font-family: "Oswald", sans-serif; font-weight: 500;
    font-size: 24px; line-height: 29px; color: var(--white);
  }
  .lead-title span { display: block; }
  .lead-title span:first-child { padding-left: 5px; }
  .lead-rule {
    position: absolute; top: 378px; left: 344px; width: 290px; height: 2px;
    background: var(--white);
  }
  .lead-points {
    position: absolute; top: 391px; left: 0; list-style: none;
    font-weight: 600; font-size: 13.5px; line-height: 21px; color: var(--white);
  }
  .lead-points li:nth-child(1) { padding-left: 341px; }
  .lead-points li:nth-child(2) { padding-left: 337px; }
  .lead-points li:nth-child(3) { padding-left: 333px; }
  .lead-points li:nth-child(4) { padding-left: 329px; }
  .join-column {
    position: absolute; left: 0; top: 449px; width: 200px; height: 420px;
    background: linear-gradient(160deg, #1d62b6 0%, var(--brand-blue) 45%, #2a6fc0 80%, #3f82cc 100%);
  }
  .join-headline {
    position: absolute; left: 29px; top: 73px;
    font-size: 29px; line-height: 33.5px; color: var(--white);
  }
  .join-headline strong { display: block; font-weight: 900; }
  .join-headline .soft { display: block; font-weight: 300; font-size: 24px; }
  .licensed {
    position: absolute; left: 31px; top: 347px;
    font-weight: 400; font-size: 11.5px; line-height: 16.5px; color: var(--white);
  }
  .offer-title {
    position: absolute; left: 239px; top: 510px;
    font-weight: 900; font-size: 30px; color: var(--orange); letter-spacing: .3px;
  }
  .offer-list {
    position: absolute; left: 247px; top: 555px; list-style: none;
    font-family: "Oswald", sans-serif; font-weight: 500;
    font-size: 15.5px; line-height: 27.7px; color: var(--list-blue);
  }
  .offer-list li { display: flex; align-items: center; }
  .offer-list svg { width: 14px; height: 14px; margin-right: 11px; flex: none; }
  .contact-bar {
    position: absolute; left: 0; top: 869px; width: 690px; height: 70px;
    background: var(--footer-grey);
    font-weight: 600; color: var(--royal-blue);
  }
  .contact-item { position: absolute; display: flex; align-items: center; }
  .contact-item svg { flex: none; margin-right: 9px; }
  .contact-address { left: 40px; top: 18px; font-size: 11.5px; line-height: 16px; }
  .contact-phone { left: 292px; top: 25px; font-size: 13.5px; }
  .contact-email { left: 450px; top: 26px; font-size: 12.5px; }
</style>
</head>
<body>
<main class="flyer">
  <div class="hero-photo" role="img" aria-label="Silhouettes of business professionals blended with a bright city skyline"></div>
  <div class="brand-name"><span class="mark"></span>Marlow Realty</div>

  <svg class="lead-panel" width="690" height="500" viewBox="0 0 690 500" aria-hidden="true">
    <polygon points="280,449 314,449 314,490 306,490" fill="var(--deep-navy)"/>
    <polygon points="314,295 690,295 690,490 287,490" fill="var(--brand-blue)"/>
  </svg>

  <div class="commission-band">100% COMMISSION<br>NO MONTHLY FEE</div>

  <h2 class="lead-title"><span>LEAD GENERATION SOFTWARE</span><span>WITH OVER 3,000 LEADS</span></h2>
  <div class="lead-rule"></div>
  <ul class="lead-points">
    <li>- 10 LEADS TO START</li>
    <li>- FREE PERSONAL CRM AND WEBSITE</li>
    <li>- RESTRICTIONS AND RULES APPLY</li>
    <li>- $450 FLAT TRANSACTION FEE</li>
  </ul>

  <section class="join-column" role="img" aria-label="Faint photo of smiling real estate agents under a blue overlay">
    <h1 class="join-headline">
      <strong>JOIN</strong><strong>OUR</strong><strong>WINNING</strong><strong>TEAM</strong>
      <span class="soft">OF</span><span class="soft">AGENTS</span><span class="soft">TODAY!</span>
    </h1>
    <p class="licensed">LICENSED IN<br>D.C., MARYLAND,<br>AND VIRGINIA</p>
  </section>

  <h2 class="offer-title">WHAT WE OFFER</h2>
  <ul class="offer-list">
    <li><svg viewBox="0 0 14 14"><rect x="1" y="2" width="11" height="11" fill="none" stroke="var(--list-blue)" stroke-width="1.4"/><path d="M3.5 7l3 3L13 2.5" fill="none" stroke="var(--list-blue)" stroke-width="1.6"/></svg>24/7 OFFICE ACCESS</li>
    <li><svg viewBox="0 0 14 14"><rect x="1" y="2" width="11" height="11" fill="none" stroke="var(--list-blue)" stroke-width="1.4"/><path d="M3.5 7l3 3L13 2.5" fill="none" stroke="var(--list-blue)" stroke-width="1.6"/></svg>FREE E &amp; O INSURANCE FOR 1ST YEAR</li>
    <li><svg viewBox="0 0 14 14"><rect x="1" y="2" width="11" height="11" fill="none" stroke="var(--list-blue)" stroke-width="1.4"/><path d="M3.5 7l3 3L13 2.5" fill="none" stroke="var(--list-blue)" stroke-width="1.6"/></svg>FREE ONLINE CE AND PLE</li>
    <li><svg viewBox="0 0 14 14"><rect x="1" y="2" width="11" height="11" fill="none" stroke="var(--list-blue)" stroke-width="1.4"/><path d="M3.5 7l3 3L13 2.5" fill="none" stroke="var(--list-blue)" stroke-width="1.6"/></svg>FREE 1,000 BUSINESS CARDS</li>
    <li><svg viewBox="0 0 14 14"><rect x="1" y="2" width="11" height="11" fill="none" stroke="var(--list-blue)" stroke-width="1.4"/><path d="M3.5 7l3 3L13 2.5" fill="none" stroke="var(--list-blue)" stroke-width="1.6"/></svg>FREE PROFESSIONAL SOCIAL MEDIA MARKETING</li>
    <li><svg viewBox="0 0 14 14"><rect x="1" y="2" width="11" height="11" fill="none" stroke="var(--list-blue)" stroke-width="1.4"/><path d="M3.5 7l3 3L13 2.5" fill="none" stroke="var(--list-blue)" stroke-width="1.6"/></svg>FREE PRINTING, SCANNING, AND COPIES</li>
    <li><svg viewBox="0 0 14 14"><rect x="1" y="2" width="11" height="11" fill="none" stroke="var(--list-blue)" stroke-width="1.4"/><path d="M3.5 7l3 3L13 2.5" fill="none" stroke="var(--list-blue)" stroke-width="1.6"/></svg>FREE BUYER AND SELLER PRESENTATION PACKAGES</li>
    <li><svg viewBox="0 0 14 14"><rect x="1" y="2" width="11" height="11" fill="none" stroke="var(--list-blue)" stroke-width="1.4"/><path d="M3.5 7l3 3L13 2.5" fill="none" stroke="var(--list-blue)" stroke-width="1.6"/></svg>FREE FILQUAY CLOUD BASED DOCUMENT MANAGEMENT ACCESS</li>
    <li><svg viewBox="0 0 14 14"><rect x="1" y="2" width="11" height="11" fill="none" stroke="var(--list-blue)" stroke-width="1.4"/><path d="M3.5 7l3 3L13 2.5" fill="none" stroke="var(--list-blue)" stroke-width="1.6"/></svg>ACCESS TO OUR INTERNAL BROKERAGE FORUM</li>
    <li><svg viewBox="0 0 14 14"><rect x="1" y="2" width="11" height="11" fill="none" stroke="var(--list-blue)" stroke-width="1.4"/><path d="M3.5 7l3 3L13 2.5" fill="none" stroke="var(--list-blue)" stroke-width="1.6"/></svg>COMPANY PROFIT SHARING!</li>
    <li><svg viewBox="0 0 14 14"><rect x="1" y="2" width="11" height="11" fill="none" stroke="var(--list-blue)" stroke-width="1.4"/><path d="M3.5 7l3 3L13 2.5" fill="none" stroke="var(--list-blue)" stroke-width="1.6"/></svg>PRIVATE OFFICES AVAILABLE TO RENT</li>
  </ul>

  <footer class="contact-bar">
    <div class="contact-item contact-address">
      <svg width="12" height="16" viewBox="0 0 12 16"><path d="M6 0C2.7 0 0 2.6 0 5.9 0 10 6 16 6 16s6-6 6-10.1C12 2.6 9.3 0 6 0zm0 8.3a2.4 2.4 0 1 1 0-4.8 2.4 2.4 0 0 1 0 4.8z" fill="var(--royal-blue)"/></svg>
      <span>4817 AMBERFIELD ROAD,<br>SUITE 512, FAIRFAX, VA 22194</span>
    </div>
    <div class="contact-item contact-phone">
      <svg width="12" height="16" viewBox="0 0 12 16"><path d="M3 0l2.4 3.8-1.6 1.8c.6 2 1.9 4 3.6 5.2l1.8-1.3L12 12l-1.6 3.3C4.6 15.5.2 8.6 1 1.5z" fill="var(--royal-blue)"/></svg>
      <span>703-555-0147</span>
    </div>
    <div class="contact-item contact-email">
      <svg width="17" height="12" viewBox="0 0 17 12"><rect width="17" height="12" fill="var(--royal-blue)"/><path d="M0.5 0.8L8.5 7l8-6.2" fill="none" stroke="var(--footer-grey)" stroke-width="1.4"/></svg>
      <span>info@marlowrealty.example</span>
    </div>
  </footer>
</main>
</body>
</html>
```